Creative label for amber glass candle jar.

We are a candle company. Our products are handmade by us and natural. We are looking for something minimalistic and unique. We need a label for our candle jars (amber glass with black lid). Our current label doesn't match these requirements. We would like our products to be stocked in London shop, therefore design has to be up to a high standard. Jar specification Diameter (mm) 65 Height without cap (mm) 80. We want the new design to be different from the current one. It's just a guide for wording.
We should be able adjust the label, to change scent name.
Our scents are
*Coconut & Vanilla
*Lavender
*Bergamot
*Italian Garden
*Hygge
*Eucalyptus & Peppermint
*Coffee
*Cedarwood & Juniperberry
To know more about us, visit our website www.fenwickbrae.com or instagram.com/fenwickbrae
Good luck!
Industry/Entity Type
It Company
Colors
Designer to choose colors to be used in the design.
Requirements
Must have
- * I have attached two of our logos, label design must include one of them.
- *has to mention that it's made in London
- *has to say that candle is natural/made with essential oils
- *has to have scent name and No. on it..
- Label can be vertical or horizontal, but has to be square/rectangular,.
Should not have
- Label should not be round

```html
<!DOCTYPE html>
<html lang="en">
<head>
<meta charset="utf-8">
<title>Quelvo Candle Labels</title>
<link rel="stylesheet" href="https://fonts.googleapis.com/css2?family=Share+Tech+Mono&family=Montserrat:wght@600&display=swap">
<style>
  :root {
    --page: #ffffff;
    --label: #1c1c1c;
    --ink: #ffffff;
  }
  html, body {
    margin: 0;
    padding: 0;
    width: 1200px;
    height: 1200px;
    overflow: hidden;
    background: var(--page);
  }
  .sheet {
    position: relative;
    width: 1200px;
    height: 1200px;
  }
  .label {
    position: absolute;
    left: 326px;
    width: 548px;
    height: 497px;
    background: var(--label);
    border-radius: 13px;
    color: var(--ink);
    font-family: "Share Tech Mono", monospace;
  }
  .label--first { top: 66px; }
  .label--second { top: 642px; }
  .brand {
    position: absolute;
    top: 44px;
    left: 0;
    right: 0;
    text-align: center;
    font-size: 60px;
    line-height: 64px;
    letter-spacing: 4px;
  }
  .scent-name {
    position: absolute;
    left: 36px;
    top: 174px;
    margin: 0;
    font-weight: 400;
    font-size: 50px;
    line-height: 55px;
    letter-spacing: 3px;
  }
  .rule {
    position: absolute;
    left: 37px;
    top: 294px;
    width: 270px;
    height: 2px;
    background: var(--ink);
  }
  .claim {
    position: absolute;
    left: 38px;
    top: 302px;
    margin: 0;
    font-size: 15px;
    line-height: 18px;
    letter-spacing: 1.9px;
  }
  .origin {
    position: absolute;
    left: 30px;
    bottom: 20px;
    font-family: "Montserrat", sans-serif;
    font-weight: 600;
    font-size: 21px;
    letter-spacing: -0.6px;
  }
  .number {
    position: absolute;
    right: 18px;
    bottom: 14px;
    display: flex;
    align-items: baseline;
  }
  .number__prefix {
    font-size: 24px;
    letter-spacing: 2px;
  }
  .number__value {
    font-size: 60px;
    line-height: 48px;
    letter-spacing: 3px;
  }
</style>
</head>
<body>
<main class="sheet">
  <section class="label label--first">
    <div class="brand">quelvo</div>
    <h2 class="scent-name">Italian<br>Garden</h2>
    <div class="rule"></div>
    <p class="claim">Made with essential oils<br>&amp; 100% Natural</p>
    <div class="origin">MADE IN LONDON</div>
    <div class="number"><span class="number__prefix">NO.</span><span class="number__value">03</span></div>
  </section>

  <section class="label label--second">
    <div class="brand">quelvo</div>
    <h2 class="scent-name">Cedarwood &amp;<br>Juniperberry</h2>
    <div class="rule"></div>
    <p class="claim">Made with essential oils<br>&amp; 100% Natural</p>
    <div class="origin">MADE IN LONDON</div>
    <div class="number"><span class="number__prefix">NO.</span><span class="number__value">07</span></div>
  </section>
</main>
</body>
</html>
```